Business Card Design

The attached file is what i need on the front of the card. No details to be changed.

On the back could i have as a heading:
We buy for cash $$$
Deceased estates house lots
Antiques, vintage furniture, bikes, kitchenware, automobile, toys,
sports memorabilia, books, records, signage,farm equipment and fashion.

Industry/Entity Type

House

```html
<!DOCTYPE html>
<html lang="en">
<head>
<meta charset="utf-8">
<title>Maple Lane Vintage – Business Card</title>
<link href="https://fonts.googleapis.com/css2?family=Open+Sans:wght@400;600;700&display=swap" rel="stylesheet">
<style>
  :root {
    --card-red: #ee1c25;
    --deep-red: #c8141c;
    --card-white: #ffffff;
    --ink: #1a1a1a;
    --backdrop: #dcd5ca;
  }
  * { box-sizing: border-box; margin: 0; padding: 0; }
  html, body { width: 1200px; height: 843px; overflow: hidden; }
  body {
    background: var(--backdrop);
    font-family: "Open Sans", Arial, sans-serif;
    position: relative;
  }
  .card {
    position: absolute;
    width: 700px;
    border-radius: 28px;
    overflow: hidden;
    box-shadow: 0 6px 14px rgba(0,0,0,0.25);
  }
  /* Front */
  .card-front {
    left: 30px; top: 24px; height: 430px;
    background: var(--card-white);
    z-index: 2;
  }
  .front-banner {
    height: 205px;
    background: var(--card-red);
    display: flex;
    flex-direction: column;
    align-items: center;
    justify-content: center;
    gap: 16px;
  }
  .brand-name {
    color: var(--card-white);
    font-weight: 700;
    font-size: 54px;
    letter-spacing: 1px;
    display: flex;
    align-items: center;
    gap: 18px;
  }
  .brand-mark {
    width: 20px; height: 20px; border-radius: 50%;
    background: var(--card-white);
  }
  .brand-tagline {
    width: 90%;
    text-align: center;
    background: var(--deep-red);
    color: var(--card-white);
    font-weight: 600;
    font-size: 20px;
    padding: 4px 0;
  }
  .front-details {
    display: flex;
    padding: 18px 0 0 28px;
    gap: 22px;
  }
  .opening-hours { width: 160px; padding-top: 14px; }
  .opening-hours .days {
    color: var(--card-red); font-weight: 700; font-size: 19px; line-height: 1.4;
  }
  .opening-hours .times { color: var(--ink); font-weight: 600; font-size: 16px; margin-top: 2px; }
  .opening-hours .closed { color: var(--card-red); font-weight: 700; font-size: 16px; }
  .contact-list { list-style: none; }
  .contact-list li {
    display: flex; align-items: center; gap: 22px;
    font-size: 18.5px; font-weight: 600; color: var(--ink);
    height: 31px;
  }
  .contact-list svg { width: 18px; height: 18px; flex: none; }

  /* Back */
  .card-back {
    left: 470px; top: 430px; height: 400px;
    background: var(--card-red);
    color: var(--card-white);
    padding: 56px 0 0 70px;
    z-index: 1;
  }
  .buy-heading { font-weight: 700; font-size: 27px; margin-bottom: 10px; }
  .buy-list { list-style: none; }
  .buy-list li {
    position: relative;
    font-weight: 600; font-size: 20.5px; line-height: 30px;
    padding-left: 40px;
    text-transform: uppercase;
  }
  .buy-list li::before {
    content: ""; position: absolute; left: 0; top: 13px;
    width: 6px; height: 6px; border-radius: 50%; background: var(--card-white);
  }
</style>
</head>
<body>

<section class="card card-front" aria-label="Card front">
  <header class="front-banner">
    <div class="brand-name"><span class="brand-mark"></span>Maple Lane Vintage</div>
    <div class="brand-tagline">Vintage - Retro Clothing &amp; Collectables</div>
  </header>
  <div class="front-details">
    <div class="opening-hours">
      <p class="days">OPEN<br>6 DAYS<br>A WEEK</p>
      <p class="times">10:00am 5:00pm</p>
      <p class="closed">CLOSED TUESDAYS</p>
    </div>
    <ul class="contact-list">
      <li><svg viewBox="0 0 18 18"><rect x="5" y="1" width="8" height="16" rx="1.5" fill="none" stroke="#1a1a1a" stroke-width="2"/><circle cx="9" cy="14" r="1" fill="#1a1a1a"/></svg>55 012 345</li>
      <li><svg viewBox="0 0 18 18"><path d="M4 1l3 4-2 2c1 3 3 5 6 6l2-2 4 3-2 3C8 17 1 10 1 3z" fill="#1a1a1a"/></svg>0400 123 987</li>
      <li><svg viewBox="0 0 18 18"><path d="M9 1a6 6 0 0 0-6 6c0 5 6 10 6 10s6-5 6-10a6 6 0 0 0-6-6z" fill="#1a1a1a"/><circle cx="9" cy="7" r="2.2" fill="#fff"/></svg>88 Harbour View Rd. Millbrook 3900</li>
      <li><svg viewBox="0 0 18 18"><rect x="1" y="3" width="16" height="12" fill="#1a1a1a"/><path d="M1 3l8 7 8-7" fill="none" stroke="#fff" stroke-width="1.5"/></svg>info@maplelanevintage.example</li>
      <li><svg viewBox="0 0 18 18"><circle cx="9" cy="9" r="7.5" fill="none" stroke="#1a1a1a" stroke-width="1.8"/><ellipse cx="9" cy="9" rx="3" ry="7.5" fill="none" stroke="#1a1a1a" stroke-width="1.5"/><path d="M1.5 9h15" stroke="#1a1a1a" stroke-width="1.5"/></svg>www.maplelanevintage.example</li>
      <li><svg viewBox="0 0 18 18"><circle cx="9" cy="9" r="7" fill="#1a1a1a"/></svg>find us on social media</li>
    </ul>
  </div>
</section>

<section class="card card-back" aria-label="Card back">
  <h2 class="buy-heading">WE BUY FOR CASH $$$</h2>
  <ul class="buy-list">
    <li>Deceased estates house lots antiques</li>
    <li>Vintage furniture</li>
    <li>Bikes</li>
    <li>Kitchenware automobile</li>
    <li>Toys</li>
    <li>Sports memorabilia</li>
    <li>Books, records</li>
    <li>Signage</li>
    <li>Farm equipment and fashion</li>
  </ul>
</section>

</body>
</html>
```